Brisbane IT support business needs our first letterhead (Contest)

Hello we are a Brisbane based Information Technology company providing support and services to small and medium sized businesses. We provide a range of services and solutions.

The business name is Harlowe Network Computing Services, or HNCS for short.

I am looking for a letterhead that looks professional (don't we all want that), but most importantly, it most utilize the colours in the logo attached, and any text used preferably in font type: HandelGotDBol.

```html
<!DOCTYPE html>
<html lang="en">
<head>
<meta charset="UTF-8">
<title>HNCS Letterhead</title>
<link href="https://fonts.googleapis.com/css2?family=Montserrat:wght@400;500;700;800&display=swap" rel="stylesheet">
<style>
  :root {
    --backdrop: #939497;
    --paper: #ffffff;
    --navy: #0f4a66;
    --orange: #ee7d22;
    --ink: #2b2b2b;
    --skyline: #e9e9eb;
    --rule: #c9c9c9;
  }
  * { margin: 0; padding: 0; box-sizing: border-box; }
  html, body {
    width: 1200px; height: 1000px; overflow: hidden;
    background: var(--backdrop);
    font-family: "Montserrat", Arial, sans-serif;
  }
  .letterhead {
    position: absolute; left: 290px; top: 62px;
    width: 620px; height: 876px;
    background: var(--paper);
    box-shadow: 0 2px 6px rgba(0,0,0,.25);
    overflow: hidden;
  }
  .brand {
    position: absolute; left: 36px; top: 80px;
    display: flex; align-items: center; gap: 10px;
  }
  .brand-mark {
    width: 14px; height: 14px;
    background: var(--navy);
  }
  .brand-name {
    font-weight: 700; font-size: 15px; line-height: 1.2;
    color: var(--navy);
  }
  .contact {
    position: absolute; right: 26px; top: 46px;
    display: flex; align-items: flex-start; gap: 8px;
    font-size: 7.5px; color: var(--ink);
  }
  .contact-address { font-style: normal; text-align: right; margin-top: 16px; line-height: 1.3; }
  .contact-list {
    list-style: none; border-left: 1px solid var(--rule);
    padding-left: 6px; line-height: 1;
  }
  .contact-list li { display: flex; align-items: center; gap: 5px; margin-bottom: 3px; }
  .contact-icon {
    width: 9px; height: 9px; border-radius: 50%; background: var(--navy);
    display: inline-flex; align-items: center; justify-content: center;
  }
  .skyline {
    position: absolute; right: 0; bottom: 30px;
    width: 300px; height: 150px;
    background: linear-gradient(180deg, rgba(233,233,235,0) 0%, var(--skyline) 50%, var(--skyline) 100%);
  }
  .footer-band { position: absolute; left: 0; bottom: 0; width: 620px; height: 40px; }
</style>
</head>
<body>
  <main class="letterhead">
    <header>
      <div class="brand">
        <div class="brand-mark"></div>
        <div class="brand-name">Harlowe Network<br>Computing Services</div>
      </div>
      <div class="contact">
        <address class="contact-address">
          27 Alder Quay Lane<br>Eastvale, 4102, Australia
        </address>
        <ul class="contact-list">
          <li><span class="contact-icon"><svg width="6" height="6" viewBox="0 0 10 10"><path d="M2 1l2 2-1 1.5c.8 1.5 1.5 2.2 3 3L7.5 6l2 2-1.5 1.5C4 9 1 6 .5 1.5z" fill="#fff"/></svg></span>(07) 555 0148</li>
          <li><span class="contact-icon"><svg width="6" height="6" viewBox="0 0 10 10"><rect x="1" y="3" width="8" height="6" fill="#fff"/><rect x="3" y="1" width="4" height="2" fill="#fff"/></svg></span>(07) 555 0148</li>
          <li><span class="contact-icon"><svg width="6" height="6" viewBox="0 0 10 10"><rect x="1" y="2" width="8" height="6" fill="none" stroke="#fff"/><path d="M1 2l4 3 4-3" fill="none" stroke="#fff"/></svg></span>hello@hncs-mail.com</li>
          <li><span class="contact-icon"><svg width="6" height="6" viewBox="0 0 10 10"><circle cx="5" cy="5" r="4" fill="none" stroke="#fff"/><path d="M1 5h8M5 1v8" stroke="#fff"/></svg></span>www.hncs-web.com</li>
        </ul>
      </div>
    </header>

    <div class="skyline" role="img" aria-label="Faint grey city skyline with a bridge and small floating squares"></div>

    <svg class="footer-band" viewBox="0 0 620 40" aria-hidden="true">
      <polygon points="0,18 400,10 396,28 0,36" fill="var(--navy)"/>
      <polygon points="408,10 620,6 620,24 404,28" fill="var(--orange)"/>
    </svg>
  </main>
</body>
</html>
```